Dog grooming business card
This is a business card for m dog grooming business like it say above.
In the priorities box below I will have the text that I want on the card.

Industry/Entity Type

Business

Colors

Designer to choose colors to be used in the design.

Requirements
Must have
• My logo and the insurance stamp must be on the card.

Text it must have :

Professional grooming services
Email: lunabrisk@mailvane.net
Text or call 1 705 318 6642
TKV certified/member
Pet first aid certified
Next appointment ___________________________________
Nice to have
• Greens to match my logo

```html
<!DOCTYPE html>
<html lang="en">
<head>
<meta charset="utf-8">
<title>Mira Fenwick – Business Card</title>
<link href="https://fonts.googleapis.com/css2?family=Open+Sans:wght@400;700&family=Noto+Serif:wght@700&display=swap" rel="stylesheet">
<style>
  :root {
    --stage: #1e1e20;
    --card-white: #ffffff;
    --leaf-green: #8dc63f;
    --leaf-green-light: #a4d45a;
    --slate: #454547;
    --ink: #2a2a2a;
    --ink-soft: #3b3b3b;
    --badge-fill: #eef3f8;
    --badge-edge: #4a88c8;
  }
  * { margin: 0; padding: 0; box-sizing: border-box; }
  html, body {
    width: 1200px; height: 800px; overflow: hidden;
    background: var(--stage);
  }
  .stage {
    position: relative; width: 1200px; height: 800px;
    display: flex; align-items: center; justify-content: center; gap: 40px;
  }
  .card {
    position: relative; width: 520px; height: 297px; overflow: hidden;
    border-radius: 3px;
    box-shadow: 0 10px 30px rgba(0,0,0,.45);
  }
  .card-front {
    background: var(--card-white);
    display: flex; align-items: center; justify-content: center;
  }
  .brand {
    display: flex; align-items: center; gap: 16px;
  }
  .brand-dot {
    width: 46px; height: 46px; border-radius: 50%;
    background: var(--leaf-green);
  }
  .brand-name {
    font-family: "Open Sans", sans-serif; font-weight: 700;
    font-size: 40px; color: var(--ink); white-space: nowrap;
  }
  .appointment {
    position: absolute; left: 0; right: 0; bottom: 26px;
    text-align: center;
    font-family: "Open Sans", sans-serif; font-size: 12px; color: var(--ink-soft);
    white-space: nowrap;
  }
  .card-back-shapes { position: absolute; inset: 0; }
  .contact {
    position: absolute; left: 30px; top: 40px;
    font-family: "Open Sans", sans-serif; color: var(--ink);
  }
  .contact-name { font-weight: 700; font-size: 15px; }
  .contact-role { font-size: 12px; color: var(--ink-soft); margin: 0 0 12px 14px; }
  .contact-line { font-size: 12px; line-height: 22px; color: var(--ink-soft); white-space: nowrap; }
  .member-badge {
    margin-top: 12px; width: 130px; height: 56px;
    border: 1.5px solid var(--badge-edge); border-radius: 10px;
    background: var(--badge-fill);
  }
  .back-brand {
    position: absolute; left: 312px; top: 96px; width: 200px;
    display: flex; flex-direction: column; align-items: center; gap: 14px;
  }
  .back-brand .brand { gap: 8px; }
  .back-brand .brand-dot { width: 22px; height: 22px; }
  .back-brand .brand-name { font-size: 18px; color: var(--leaf-green); }
  .tagline {
    font-family: "Noto Serif", serif; font-weight: 700;
    font-size: 11px; color: var(--leaf-green); text-align: center;
    white-space: nowrap;
  }
</style>
</head>
<body>
  <main class="stage">
    <section class="card card-front" aria-label="Card front">
      <div class="brand">
        <span class="brand-dot"></span>
        <span class="brand-name">Mira Fenwick</span>
      </div>
      <p class="appointment">Next appointment ______________________________</p>
    </section>

    <section class="card card-back" aria-label="Card back">
      <svg class="card-back-shapes" viewBox="0 0 520 297" width="520" height="297" aria-hidden="true">
        <rect width="520" height="297" fill="var(--leaf-green)"/>
        <path d="M288,0 Q264,150 328,297 L520,297 L520,0 Z" fill="var(--leaf-green-light)"/>
        <path d="M300,0 Q276,150 340,297 L520,297 L520,0 Z" fill="var(--card-white)"/>
        <path d="M310,0 Q286,150 350,297 L520,297 L520,0 Z" fill="var(--slate)"/>
      </svg>

      <div class="contact">
        <p class="contact-name">Dana Pell</p>
        <p class="contact-role">Manager</p>
        <p class="contact-line">Text or call 1 705 318 6642</p>
        <p class="contact-line">Email: lunabrisk@mailvane.net</p>
        <p class="contact-line">Pet first aid certified</p>
        <p class="contact-line">TKV certified/member</p>
        <div class="member-badge" role="img" aria-label="Insurance membership stamp"></div>
      </div>

      <div class="back-brand">
        <div class="brand">
          <span class="brand-dot"></span>
          <span class="brand-name">Mira Fenwick</span>
        </div>
        <p class="tagline">Professional grooming services</p>
      </div>
    </section>
  </main>
</body>
</html>
```